Larkfield Interiors
Stationary, Letterhead & Business Card
Larkfield Interiors -
Creative Brief
Professional
Dennis Coyle
Project Manager
478 Oakmont Avenue N.W. Fairbrook, MN 12345
dennis@larkfield-interiors-studio.com
The information is fake, once the winning design is selected I will forward the correct contact information to the designer.

```html
<!DOCTYPE html>
<html lang="en">
<head>
<meta charset="utf-8">
<title>Larkfield Interiors – Stationery Set</title>
<link href="https://fonts.googleapis.com/css2?family=Open+Sans:wght@400;600;700;800&display=swap" rel="stylesheet">
<style>
  :root {
    --bg: #2b2b2b;
    --paper: #ffffff;
    --orange: #f39200;
    --orange-deep: #e07b00;
    --yellow: #ffc629;
    --grey-text: #555555;
    --grey-light: #d9d9d9;
  }
  * { margin: 0; padding: 0; box-sizing: border-box; }
  html, body { width: 1200px; height: 874px; overflow: hidden; background: var(--bg); }
  body { position: relative; font-family: "Open Sans", Arial, sans-serif; color: var(--grey-text); }

  .sheet { position: absolute; background: var(--paper); overflow: hidden; }

  .brand { display: flex; align-items: center; gap: 6px; }
  .brand-square { width: 14px; height: 14px; background: var(--orange); flex: none; }
  .brand-name { font-weight: 800; color: var(--orange); font-size: 17px; letter-spacing: .3px; white-space: nowrap; }

  .mosaic {
    position: absolute; left: 0; right: 0;
    background: linear-gradient(90deg, var(--orange-deep), var(--orange) 40%, var(--yellow) 75%, #ffe08a);
  }

  /* Envelope front */
  .envelope-front { left: 67px; top: 72px; width: 521px; height: 190px; }
  .envelope-front .brand { position: absolute; left: 28px; top: 26px; }
  .envelope-front .return-address { position: absolute; left: 48px; top: 50px; font-size: 6.5px; line-height: 1.5; color: var(--grey-text); }
  .envelope-front .mosaic { bottom: 18px; height: 34px; }

  /* Envelope back */
  .envelope-back { left: 67px; top: 272px; width: 521px; height: 230px; background: #f4f4f4; }
  .envelope-back svg.flap { position: absolute; inset: 0; }
  .envelope-back .brand { position: absolute; left: 32px; top: 132px; opacity: .35; }
  .envelope-back .brand-name { font-size: 24px; }
  .envelope-back .brand-square { width: 20px; height: 20px; }

  /* Business card front */
  .card-front { left: 67px; top: 612px; width: 238px; height: 180px; background: var(--orange); }
  .card-front .logo-panel { position: absolute; left: 0; top: 0; width: 170px; height: 52px; background: var(--paper); padding: 20px 0 0 12px; }
  .card-front .brand { gap: 5px; }
  .card-front .brand-name { font-size: 9.5px; }
  .card-front .brand-square { width: 9px; height: 9px; }
  .card-front .mosaic { top: 0; left: 170px; height: 52px; background: linear-gradient(90deg, var(--yellow), #ffe08a); }
  .card-front .person { position: absolute; left: 14px; top: 100px; color: var(--paper); }
  .card-front .person-name { font-weight: 700; font-size: 14px; }
  .card-front .person-role { font-size: 7px; margin-top: 1px; }
  .card-front .details { position: absolute; left: 14px; top: 138px; font-size: 5.8px; line-height: 1.45; color: var(--paper); }

  /* Business card back */
  .card-back { left: 319px; top: 612px; width: 238px; height: 180px;
    background: linear-gradient(135deg, #ffffff, #d8d8d8); display: flex; align-items: center; justify-content: center; }
  .card-back .brand-name { font-size: 15px; }

  /* Letterhead */
  .letterhead { left: 629px; top: 72px; width: 535px; height: 773px; }
  .letterhead .brand { position: absolute; left: 26px; top: 30px; }
  .letterhead .brand-name { font-size: 22px; }
  .letterhead .brand-square { width: 18px; height: 18px; }
  .letterhead .contact-line { position: absolute; left: 26px; top: 68px; font-size: 5.3px; white-space: nowrap; color: var(--grey-text); }
  .letterhead .rule { position: absolute; left: 26px; right: 26px; top: 78px; height: 1px; background: var(--grey-light); }
  .letterhead .body { position: absolute; left: 26px; right: 30px; top: 92px; font-size: 8.2px; line-height: 1.5; }
  .letterhead .body p { margin-bottom: 9px; }
  .letterhead .signature { position: absolute; left: 26px; top: 610px; font-size: 7.4px; border-top: 1px solid var(--grey-text); padding-top: 3px; width: 70px; }
  .letterhead .mosaic { bottom: 0; height: 80px; }
  .letterhead svg.wave { position: absolute; left: 0; bottom: 0; width: 535px; height: 100px; }
</style>
</head>
<body>

  <section class="sheet envelope-front">
    <div class="brand"><span class="brand-square"></span><span class="brand-name">LARKFIELD INTERIORS</span></div>
    <div class="return-address">
      478 Oakmont Avenue N.W.<br>
      Fairbrook, MN 12345<br>
      Phone: 555-014-2200
    </div>
    <div class="mosaic" role="img" aria-label="Band of small orange and yellow squares"></div>
  </section>

  <section class="sheet envelope-back">
    <svg class="flap" viewBox="0 0 521 230" preserveAspectRatio="none" aria-hidden="true">
      <polyline points="0,0 260,120 521,0" fill="#ffffff" stroke="#dcdcdc" stroke-width="1.5"/>
      <line x1="0" y1="230" x2="190" y2="110" stroke="#e2e2e2" stroke-width="1"/>
      <line x1="521" y1="230" x2="330" y2="110" stroke="#e2e2e2" stroke-width="1"/>
    </svg>
    <div class="brand"><span class="brand-square"></span><span class="brand-name">LARKFIELD INTERIORS</span></div>
  </section>

  <section class="sheet card-front">
    <div class="logo-panel"><div class="brand"><span class="brand-square"></span><span class="brand-name">LARKFIELD INTERIORS</span></div></div>
    <div class="mosaic" role="img" aria-label="Band of small yellow squares"></div>
    <div class="person">
      <div class="person-name">Dennis Coyle</div>
      <div class="person-role">Project Manager</div>
    </div>
    <div class="details">
      Phone: 555-014-2200 &nbsp; Fax: 555-014-2201<br>
      Email: dennis@larkfield-interiors-studio.com<br>
      Address: 478 Oakmont Avenue N.W. Fairbrook, MN 12345
    </div>
  </section>

  <section class="sheet card-back">
    <div class="brand"><span class="brand-square"></span><span class="brand-name">LARKFIELD INTERIORS</span></div>
  </section>

  <section class="sheet letterhead">
    <div class="brand"><span class="brand-square"></span><span class="brand-name">LARKFIELD INTERIORS</span></div>
    <div class="contact-line">478 Oakmont Avenue N.W. Fairbrook, MN 12345 &nbsp; Phone: 555-014-2200 &nbsp; Fax: 555-014-2201 &nbsp; Email: dennis@larkfield-interiors-studio.com &nbsp; www.larkfield-interiors.com</div>
    <div class="rule"></div>
    <div class="body">
      <p>Because sometimes business meetings can get very long, employees inevitably find something to take their mind off the repetitive speeches and go to their happy place. Oh, that was mean, but you have to admit this is a good reason to create a comfortable meeting chair.</p>
      <p>Because sometimes business meetings can get very long, employees inevitably find something to take their mind off the repetitive speeches and go to their happy place. Oh, that was mean, but you have to admit this is a good reason to create a comfortable meeting chair. From Velmora Studio, the VM chair comes with a great look and provides even more comfort. The colors are various and the complementary cushions can be chosen to fit the chair. Here is a complementary description from the producers: "at once classic and contemporary, this meeting chair of generous proportions has a plywood shell for great comfort. VM is a distinct design that feels right in a multitude of settings. Available in natural or painted veneer, and with cushions in complementary colors. The fixed or swivel base accepts castors or feet".</p>
      <p>Because sometimes business meetings can get very long, employees inevitably find something to take their mind off the repetitive speeches and go to their happy place. Oh, that was mean, but you have to admit this is a good reason to create a comfortable meeting chair. From Velmora Studio, the VM chair comes with a great look and provides even more comfort. The colors are various and the complementary cushions can be chosen to fit the chair. Here is a complementary description from the producers: "at once classic and contemporary, this meeting chair of generous proportions has a plywood shell for great comfort. VM is a distinct design that feels right in a multitude of settings. Available in natural or painted veneer, and with cushions in complementary colors. The fixed or swivel base accepts castors or feet". At once classic and contemporary, this meeting chair of generous proportions has a plywood shell for great comfort. VM is a distinct design that feels right in a multitude of settings. Available in natural or painted veneer, and with cushions in complementary colors.</p>
      <p>Because sometimes business meetings can get very long, employees inevitably find something to take their mind off the repetitive speeches and go to their happy place. Oh, that was mean, but you have to admit this is a good reason to create a comfortable meeting chair.</p>
    </div>
    <div class="signature">Project Manager</div>
    <div class="mosaic" role="img" aria-label="Band of small orange and yellow squares"></div>
    <svg class="wave" viewBox="0 0 535 100" preserveAspectRatio="none" aria-hidden="true">
      <path d="M0,0 L535,0 L535,20 C400,50 250,10 120,40 C70,52 30,62 0,70 Z" fill="#ffffff"/>
      <path d="M0,70 C30,62 70,52 120,40 C250,10 400,50 535,20" fill="none" stroke="#f39200" stroke-width="3"/>
    </svg>
  </section>

</body>
</html>
```